Quillmarsh Property Solutions need a business card design

Hello guys. We would need a business card design asap please.
We are a start up property investment business based in London UK specialised in buying, selling, managing and letting properties and helping distressed property owners.
The name of our Business is Quillmarsh, the logo symbolises the four fundamental elements of the world (earth, air, fire and water) and so it stands for strength, stability, longevity.
We would like the business card to communicate professionalism and reliability. Many many thanks indeed for your work.

Details:

1.) Rosalind Opaleye
Property Investor
Mobile: +44(0)7700361752
Email: rosalind.quillmarsh@brindlepost.co.uk

2.) Anselm Opaleye
Property Investor
Mobile: +44(0)7700584029
Email: anselm.quillmarsh@brindlepost.co.uk

Investment

```html
<!DOCTYPE html>
<html lang="en">
<head>
<meta charset="utf-8">
<title>Quillmarsh Property Solutions — Business Card</title>
<link href="https://fonts.googleapis.com/css2?family=Nunito+Sans:wght@300;400;800&display=swap" rel="stylesheet">
<style>
  :root {
    --page-bg: #e4e2df;
    --card-face: #ececec;
    --ink: #2b2b2b;
    --ink-soft: #3c3c3c;
    --accent-red: #c8283a;
    --field-red: #d2505e;
    --field-blue: #3f7fd0;
    --field-green: #2fa557;
    --white: #ffffff;
  }
  * { box-sizing: border-box; margin: 0; padding: 0; }
  html, body {
    width: 1200px;
    height: 900px;
    overflow: hidden;
  }
  body {
    background: var(--page-bg);
    font-family: "Nunito Sans", sans-serif;
    color: var(--ink);
    display: flex;
    flex-direction: column;
    align-items: center;
    justify-content: center;
    gap: 44px;
  }
  .card {
    position: relative;
    width: 640px;
    height: 366px;
    border-radius: 4px;
    box-shadow: 0 10px 26px rgba(0, 0, 0, 0.18);
    overflow: hidden;
  }

  /* Front */
  .card--front { background: var(--card-face); }
  .brand-lockup {
    position: absolute;
    top: 56px;
    right: 52px;
    display: flex;
    align-items: center;
    gap: 12px;
  }
  .brand-lockup__dot {
    width: 14px;
    height: 14px;
    border-radius: 50%;
    background: var(--ink);
  }
  .brand-lockup__name {
    font-weight: 800;
    font-size: 20px;
    line-height: 1.1;
    letter-spacing: 0.04em;
    text-transform: uppercase;
    color: var(--ink);
  }
  .brand-lockup__name small {
    display: block;
    font-size: 11px;
    letter-spacing: 0.06em;
  }
  .holder {
    position: absolute;
    left: 52px;
    top: 160px;
    text-transform: uppercase;
    font-weight: 300;
  }
  .holder__name {
    font-size: 27px;
    letter-spacing: 0.02em;
    color: var(--ink);
  }
  .holder__role {
    font-size: 17px;
    letter-spacing: 0.03em;
    color: var(--ink-soft);
    margin-top: 2px;
  }
  .contacts {
    position: absolute;
    left: 52px;
    bottom: 46px;
    list-style: none;
    font-weight: 300;
    font-size: 16px;
    line-height: 1.5;
    color: var(--ink);
  }
  .contacts__label {
    display: inline-block;
    width: 22px;
    color: var(--accent-red);
    font-weight: 400;
  }

  /* Back */
  .card--back {
    background:
      linear-gradient(160deg, var(--field-red) 0%, rgba(210, 80, 94, 0) 48%),
      linear-gradient(215deg, var(--field-blue) 0%, rgba(63, 127, 208, 0) 52%),
      var(--field-green);
  }
  .back-field {
    position: absolute;
    inset: 0;
    display: flex;
    align-items: center;
    justify-content: center;
  }
  .back-field__name {
    font-weight: 800;
    font-size: 30px;
    letter-spacing: 0.08em;
    text-transform: uppercase;
    color: var(--white);
  }
</style>
</head>
<body>

  <section class="card card--front" aria-label="Business card front">
    <div class="brand-lockup">
      <span class="brand-lockup__dot"></span>
      <p class="brand-lockup__name">Quillmarsh<small>Property Solutions</small></p>
    </div>

    <div class="holder">
      <h1 class="holder__name">Rosalind Opaleye</h1>
      <p class="holder__role">Property Investor</p>
    </div>

    <ul class="contacts">
      <li><span class="contacts__label">m</span>+44(0)7700361752</li>
      <li><span class="contacts__label">e</span>rosalind.quillmarsh@brindlepost.co.uk</li>
    </ul>
  </section>

  <section class="card card--back" aria-label="Business card back">
    <div class="back-field" role="img" aria-label="Red, blue and green colour fields behind the company name">
      <p class="back-field__name">Quillmarsh</p>
    </div>
  </section>

</body>
</html>
```